Real Estate - Car Wrap - Graphic design work for bus advertisement

Looking for graphic design work for Martin Fairwell - Real Estate Associate. Name of the company is Fairwell Property Services. Slogan is:
Homes Found Keys Turned - We would really like to see the slogan used.

In need of an ad design that will be used for a bus ad. Bus ad specs included in attachments.

Bus ad info (Must include)
Martin Fairwell
Homeline Prime logo
Martin's phone number is 780-555-0143
Website is: Fairwellproperty.example
I have included the bus ad dimensions in the attachments

Our color scheme is Black & White with a hint of Navy Blue and we are open to a little bit of gold to add a little bit of color. We like the idea of the ad being in black and white and then just adding a hint of blue. Martins photo might be nice black and white. Open to ideas on this.

The final design should communicate professionalism, strength and approachability while being eye catching with a bit of wow factor. Something clean and modern with potentially some interesting graphic work.

Our ad design must incorporate the Homeline Prime Logo doesn't have to be in the color red like attached photo. It can be in any color that goes well with the ad just needs to be present.

We love the attached ad idea that I have included to help give some idea of where we are going. No purple however we want to stick with the Navy as the main color choice.

The dimensions for the bus ad are are attached in specs for the bus.
We really like the idea of using the head shot of Martin standing in the blue shirt for the bus ad, (can be in color or black and white) We are however open to the other photo in attachments. Looking to see what you come up with.

I have included Martin's name written in more of a signature font like the ad idea has. We want something in more of a signature for his name. See Signature for Martin Fairwell for ex. Something as close to this as possible. Needs to be very easy to read from afar. Please don't include the strength of housing that is on this photo. We don't like this slogan.

I have attached, head shots of Martin, Our companies current logo which is the house and an overall picture idea of the look we are going for. We really like this ad for an idea, black and white with a splash of color at the bottom. Again our color is Navy Blue.

Please message me if you have questions.
Thank you,

Lena Fairwell

Please note that Martin’s photo needs to be on the business card. We also do not want any purple color in the design. The ad example image is just to give an idea of something we like. Thank you

Industry/Entity Type

Real Estate Agent

Font styles to use
Script

Requirements
Must have
• Colors are black and white with accent navy
Nice to have
• Open to a hint of gold
Should not have
• Any purple or light blue colors

```html
<!DOCTYPE html>
<html lang="en">
<head>
<meta charset="utf-8">
<title>Martin Fairwell – Bus Ad</title>
<link rel="stylesheet" href="https://fonts.googleapis.com/css2?family=Open+Sans:ital,wght@0,600;0,700;1,800&display=swap">
<style>
  :root {
    --navy: #15295a;
    --navy-text: #1b2d5e;
    --white: #ffffff;
    --grey-text: #4a4a4a;
    --silver-light: #f4f4f4;
    --silver-mid: #d6d6d6;
    --silver-dark: #a9a9a9;
    --photo-light: #dcdcdc;
    --photo-mid: #9a9a9a;
    --photo-dark: #3a3a3e;
    --accent-red: #c8202f;
  }
  * { margin: 0; padding: 0; box-sizing: border-box; }
  html, body { width: 1200px; height: 539px; overflow: hidden; background: var(--white); }
  .ad {
    position: relative;
    width: 1200px;
    height: 539px;
    background: var(--white);
    font-family: "Open Sans", Arial, sans-serif;
    overflow: hidden;
  }
  .name-band {
    position: absolute;
    left: 0; top: 282px;
    width: 1200px; height: 144px;
    background: var(--navy);
  }
  .contact-band {
    position: absolute;
    left: 0; top: 426px;
    width: 1200px; height: 113px;
    background: linear-gradient(180deg, var(--silver-light) 0%, var(--silver-mid) 55%, var(--silver-dark) 100%);
  }
  .agent-photo {
    position: absolute;
    left: 66px; top: 8px;
    width: 318px; height: 531px;
    border-radius: 120px 120px 0 0;
    background: linear-gradient(180deg, var(--photo-light) 0%, var(--photo-mid) 78%, var(--photo-dark) 100%);
  }
  .slogan {
    position: absolute;
    right: 90px; top: 118px;
    font-size: 40px;
    font-weight: 800;
    font-style: italic;
    color: var(--navy-text);
    white-space: nowrap;
    line-height: 1.2;
  }
  .website {
    position: absolute;
    right: 92px; top: 176px;
    font-size: 24px;
    font-weight: 600;
    color: var(--grey-text);
    white-space: nowrap;
    letter-spacing: 0.5px;
  }
  .agent-name {
    position: absolute;
    left: 430px; top: 302px;
    font-size: 86px;
    font-weight: 800;
    font-style: italic;
    letter-spacing: 1px;
    word-spacing: 14px;
    line-height: 1.2;
    white-space: nowrap;
    background: linear-gradient(180deg, #ffffff 0%, #e6e6e6 45%, #a8a8a8 60%, #dcdcdc 100%);
    -webkit-background-clip: text;
    background-clip: text;
    color: transparent;
  }
  .brand {
    position: absolute;
    left: 446px;
    display: flex;
    align-items: center;
    gap: 8px;
    font-weight: 700;
    white-space: nowrap;
    font-size: 22px;
    line-height: 1.2;
  }
  .brand-company { top: 457px; color: var(--navy-text); }
  .brand-company .mark { width: 14px; height: 14px; background: var(--navy-text); }
  .brand-network { top: 489px; color: var(--accent-red); }
  .brand-network .mark { width: 18px; height: 18px; border-radius: 50%; background: var(--navy-text); margin-left: 4px; }
  .phone {
    position: absolute;
    left: 754px; top: 450px;
    font-size: 53px;
    font-weight: 800;
    font-style: italic;
    letter-spacing: 1px;
    color: var(--navy-text);
    white-space: nowrap;
    line-height: 1.2;
  }
</style>
</head>
<body>
  <main class="ad">
    <div class="name-band"></div>
    <div class="contact-band"></div>
    <div class="agent-photo" role="img" aria-label="Black and white photo of Martin Fairwell, smiling, arms crossed, in a checked shirt"></div>
    <p class="slogan">Homes Found Keys Turned</p>
    <p class="website">Fairwellproperty.example</p>
    <h1 class="agent-name">Martin Fairwell</h1>
    <div class="brand brand-company"><span class="mark"></span><span>Fairwell Property</span></div>
    <div class="brand brand-network"><span>Homeline Prime</span><span class="mark"></span></div>
    <p class="phone">780-555-0143</p>
  </main>
</body>
</html>
```